Locksmiths Business Card Designs needed!!

I need a business card design for my new small locksmith business.
I would love my business card to be simple, (not too many photos of locks or keys) but strong images so that everyone can recognise it is locksmithing business without reading the words.

I want all information i put in upper article to appear on front side in anyway depending on your design of suggestions and on the back side I would love to mention theses;
-24 /7 mobile services (including weekends & public holidays)
-Residential / Commercial/ Automotive
-Opening / Repair / Installation
-Cut keys

Im not a native english speaker so you can fix the words or expressions as you think it is right and natural.

I realised that in the business names, there is too many "locks" and "s" so I would love to seperate the words somehow so that it is more natural when someone read the business name on the card. for example,put the part of "Bright Harbour Trade Services" first line and the part of "Locksmiths" on the other line....I am just suggesting..doesn't need to be like that..but it should say "Locksmiths" as it is locksmiths business. :)

Target Market(s)

all generations

Industry/Entity Type

Locksmith

Contact Information for Business Card

business name : Bright Harbour Trade Services Locksmiths
ABN 46281903754
Name : Tom Reyes (바다 문)
phone : 0468 219 357
email : brightharbourtrade@mailvero.net

Requirements
Must have
• A symbol of either a key or a lock
Nice to have
• I like the symbol of a key in the photo I have attached here. So maybe, if you couldn't find any other good symbols I am happy to have the symbol on the business somehow.
Should not have
• Too many keys or locks

```html
<!DOCTYPE html>
<html lang="en">
<head>
<meta charset="utf-8">
<title>Bright Harbour Trade Services Locksmiths – Business Card</title>
<link rel="stylesheet" href="https://fonts.googleapis.com/css2?family=Arimo:wght@400;700&family=Noto+Sans+KR:wght@400&display=swap">
<style>
  :root {
    --paper: #ffffff;
    --charcoal: #3a3a3a;
    --sky: #00aeef;
    --ink-light: #ffffff;
  }
  html, body {
    margin: 0;
    padding: 0;
    overflow: hidden;
    background: var(--paper);
  }
  .card {
    position: relative;
    width: 1200px;
    height: 693px;
    background: var(--paper);
    overflow: hidden;
    font-family: "Arimo", "Noto Sans KR", Arial, sans-serif;
  }
  .brand {
    position: absolute;
    left: 70px;
    top: 95px;
    display: flex;
    align-items: center;
    gap: 40px;
  }
  .brand-dot {
    width: 120px;
    height: 120px;
    border-radius: 50%;
    background: var(--charcoal);
    flex: none;
  }
  .brand-name {
    margin: 0;
    font-family: "Arimo", Arial, sans-serif;
    font-weight: 700;
    font-size: 44px;
    line-height: 54px;
    color: var(--charcoal);
  }
  .abn {
    position: absolute;
    right: 60px;
    top: 306px;
    margin: 0;
    font-size: 31px;
    line-height: 40px;
    color: var(--charcoal);
  }
  .abn-label { color: var(--sky); }
  .divider {
    position: absolute;
    left: 0;
    top: 350px;
    width: 1200px;
    height: 15px;
    background: var(--sky);
  }
  .contact-panel {
    position: absolute;
    left: 0;
    top: 365px;
    width: 1200px;
    height: 328px;
    background: var(--charcoal);
    color: var(--ink-light);
  }
  .holder {
    position: absolute;
    left: 65px;
    top: 42px;
    margin: 0;
    font-size: 43px;
    font-weight: 400;
    line-height: 52px;
  }
  .holder-korean { font-family: "Noto Sans KR", "Arimo", sans-serif; }
  .contact-line {
    position: absolute;
    left: 58px;
    display: flex;
    align-items: center;
    gap: 14px;
    font-size: 38px;
    line-height: 46px;
    margin: 0;
  }
  .contact-phone { top: 180px; }
  .contact-email { top: 230px; }
  .contact-icon { flex: none; }
</style>
</head>
<body>
<main class="card">
  <header class="brand">
    <span class="brand-dot" aria-hidden="true"></span>
    <h1 class="brand-name">Bright Harbour Trade Services<br>Locksmiths</h1>
  </header>

  <p class="abn"><span class="abn-label">ABN</span> 46281903754</p>

  <div class="divider"></div>

  <section class="contact-panel">
    <p class="holder">Tom Reyes (<span class="holder-korean">바다 문</span>)</p>

    <p class="contact-line contact-phone">
      <svg class="contact-icon" width="28" height="28" viewBox="0 0 28 28" aria-hidden="true">
        <rect x="0" y="0" width="28" height="28" rx="5" fill="#00aeef"/>
        <path d="M10 6 C7 7 6.5 10 8 14 C9.5 18 12 21 15.5 22.5 L18 20 L15.5 17.5 L13.8 18.6 C12.2 17.3 11 15.3 10.6 13.4 L12.4 12.2 L11.5 8.5 Z" fill="#3a3a3a"/>
      </svg>
      <span>0468 219 357</span>
    </p>

    <p class="contact-line contact-email">
      <svg class="contact-icon" width="30" height="20" viewBox="0 0 30 20" aria-hidden="true">
        <rect x="0" y="0" width="30" height="20" fill="#00aeef"/>
        <path d="M0 0 L15 11 L30 0" fill="none" stroke="#3a3a3a" stroke-width="2"/>
      </svg>
      <span>brightharbourtrade@mailvero.net</span>
    </p>
  </section>
</main>
</body>
</html>
```